Glitterstars & Spinqueens 4x6 Flyer

We need a flyer for an exotic dance event near Milwaukee, WI called Glitterstars & Spinqueens. The event is a showcase of exotic talent.

The design should be inviting to those ladies that want to perform and the audience that will attend.

I'm open to any color scheme or artistic style with the design.

Information for the flyer:

Velvet Lantern Presents:
Glitterstars & Spinqueens
A Glamworks Showcase

Sunday April 19th Show Starts @ 7pm
Hosted By Rick Dellano
With A Headlining Performance From 2x Twirlmania Queen of the Pole & KLV Competitor LORNA VEX

A Night Of Erotic Talent With Ladies From Across The Midwest

Amateurs, Award Winning Performers and All Those In Between!

Exotic Dancers and Pole Dancers Performing Live On Stage

To register and more info contact us glamworks-example.info

Velvet lantern 20568 N 14th Ave Franklin,WI 414-555-0193
Vlx.club/ rickdellano-example.com/cosmicwombat-example.com/ FB(logo)/milwaukeevlx

Velvet lantern Logo (largest logo in the design)
Cosmic Wombat Logo, Glamworks Logo (much smaller than the VLX logo)

```html
<!DOCTYPE html>
<html lang="en">
<head>
<meta charset="utf-8">
<title>Glitterstars &amp; Spinqueens Flyer</title>
<link href="https://fonts.googleapis.com/css2?family=Audiowide&family=Oswald:wght@500;700&family=Questrial&family=Poiret+One&display=swap" rel="stylesheet">
<style>
  :root {
    --navy: #0a0e2a;
    --deep: #05071a;
    --cyan: #35c8f2;
    --white: #ffffff;
    --gold-light: #fff1b8;
    --gold: #f2b13a;
    --gold-dark: #b86a12;
    --orange: #ff7a1a;
    --red: #d9241c;
    --violet: #5a2fb8;
    --skin: #c98a6a;
    --hair: #3a1a12;
    --rule: rgba(255,255,255,0.75);
    --muted: #c9cbd8;
  }
  * { margin: 0; padding: 0; box-sizing: border-box; }
  html, body { width: 819px; height: 1200px; overflow: hidden; background: var(--deep); }
  .flyer {
    position: relative; width: 819px; height: 1200px; overflow: hidden;
    background:
      radial-gradient(ellipse 360px 240px at 300px 660px, rgba(255,160,40,0.8), rgba(255,90,20,0.3) 55%, transparent 80%),
      radial-gradient(ellipse 260px 200px at 560px 760px, rgba(217,36,28,0.7), transparent 75%),
      radial-gradient(ellipse 320px 280px at 110px 560px, rgba(60,110,230,0.65), transparent 75%),
      radial-gradient(ellipse 300px 260px at 720px 460px, rgba(90,47,184,0.55), transparent 75%),
      linear-gradient(180deg, var(--navy) 0%, #121a4a 45%, #1a0f2a 75%, var(--deep) 86%);
    font-family: "Questrial", sans-serif; color: var(--white);
  }
  .top-bar {
    position: absolute; left: 0; top: 0; width: 100%; height: 118px;
    background: rgba(5,7,26,0.6); padding: 18px 30px 0;
  }
  .date-line { font-family: "Oswald", sans-serif; font-weight: 700; font-size: 23px; line-height: 1.2; text-transform: uppercase; }
  .date-line .day { color: var(--cyan); }
  .host-line { font-family: "Oswald", sans-serif; font-weight: 500; font-size: 17px; line-height: 1.3; margin-top: 3px; }
  .headliner-line { font-family: "Oswald", sans-serif; font-weight: 500; font-size: 13.5px; line-height: 1.3; margin-top: 6px; }
  .performer-photo {
    position: absolute; left: 400px; top: 118px; width: 410px; height: 830px;
    background:
      radial-gradient(ellipse 150px 360px at 215px 400px, rgba(201,138,106,0.75), rgba(58,26,18,0.55) 60%, transparent 90%);
  }
  .club-mark { position: absolute; left: 30px; top: 232px; width: 360px; }
  .presents-line { font-family: "Oswald", sans-serif; font-weight: 500; font-size: 15px; letter-spacing: 2px; text-transform: uppercase; color: var(--cyan); }
  .club-name {
    font-family: "Oswald", sans-serif; font-weight: 700; color: var(--white);
    font-size: 54px; line-height: 0.98; text-transform: uppercase; margin-top: 4px;
  }
  .club-tagline { font-family: "Oswald", sans-serif; font-weight: 500; font-size: 18px; margin-top: 6px; }
  .event-name {
    position: absolute; left: 30px; top: 420px; width: 380px;
    font-family: "Oswald", sans-serif; font-weight: 700; font-size: 30px; line-height: 1.1;
    text-transform: uppercase; color: var(--gold);
  }
  .showcase-line { position: absolute; left: 30px; top: 458px; font-family: "Oswald", sans-serif; font-weight: 500; font-size: 17px; letter-spacing: 1px; }
  .event-title {
    position: absolute; left: 30px; top: 505px; width: 770px;
    font-family: "Audiowide", sans-serif; font-weight: 400; text-transform: uppercase;
    background: linear-gradient(180deg, var(--gold-light) 0%, var(--gold) 55%, var(--gold-dark) 100%);
    -webkit-background-clip: text; background-clip: text; color: transparent;
  }
  .event-title .line-one { display: block; font-size: 64px; line-height: 82px; }
  .event-title .line-two { display: block; font-size: 58px; line-height: 78px; }
  .event-sub { position: absolute; left: 54px; top: 684px; font-size: 32px; line-height: 1.2; }
  .rule { position: absolute; left: 30px; width: 759px; height: 2px; background: var(--rule); }
  .rule.first { top: 772px; }
  .rule.second { top: 954px; }
  .lineup { position: absolute; left: 30px; top: 795px; width: 740px; font-size: 25px; line-height: 1.36; }
  .partner-mark {
    position: absolute; left: 565px; top: 905px; padding: 2px 10px;
    background: var(--white); color: #1d3fb0;
    font-family: "Oswald", sans-serif; font-weight: 700; font-size: 22px; line-height: 1.3;
  }
  .category-row { position: absolute; left: 30px; top: 1008px; width: 760px; font-size: 40px; line-height: 1.2; letter-spacing: 1px; white-space: nowrap; }
  .category-row .bold { font-family: "Oswald", sans-serif; font-weight: 700; }
  .category-row .thin { font-family: "Poiret One", sans-serif; font-weight: 400; }
  .contact { position: absolute; left: 30px; top: 1096px; width: 600px; font-size: 14.5px; line-height: 1.95; color: var(--muted); }
  .contact strong { color: var(--white); font-weight: 400; }
  .social-square { display: inline-block; width: 13px; height: 13px; background: var(--muted); vertical-align: -1px; margin: 0 4px; }
  .sponsor-mark {
    position: absolute; left: 648px; top: 1068px; width: 142px; height: 120px;
    background: var(--deep); display: flex; flex-direction: column; align-items: center; justify-content: center; gap: 6px;
  }
  .sponsor-mark .square { width: 56px; height: 56px; background: var(--red); }
  .sponsor-mark .name { font-family: "Oswald", sans-serif; font-weight: 700; font-size: 16px; color: var(--red); text-transform: uppercase; }
</style>
</head>
<body>
<main class="flyer">
  <header class="top-bar">
    <p class="date-line"><span class="day">Sunday</span> April 19th Show Starts @ 7pm</p>
    <p class="host-line">Hosted By RICK DELLANO</p>
    <p class="headliner-line">With A Headlining Performance From 2x Twirlmania Queen of the Pole &amp; KLV Competitor LORNA VEX</p>
  </header>

  <div class="performer-photo" role="img" aria-label="Photo of the headlining dancer posing in a studded bikini top"></div>

  <div class="club-mark">
    <p class="presents-line">Velvet Lantern Presents:</p>
    <p class="club-name">Velvet Lantern</p>
    <p class="club-tagline">Midwest's Premier Gentlemen's Club</p>
  </div>

  <p class="event-name">Glitterstars &amp; Spinqueens</p>
  <p class="showcase-line">A Glamworks Showcase</p>

  <h1 class="event-title"><span class="line-one">A Night</span><span class="line-two">Of Erotic Talent</span></h1>
  <p class="event-sub">With Ladies From Across The Midwest</p>

  <div class="rule first"></div>
  <p class="lineup">Amateurs, Award Winning Performers and All Those In Between! Exotic Dancers and Pole Dancers Performing Live On Stage</p>
  <div class="partner-mark">Glamworks</div>
  <div class="rule second"></div>

  <p class="category-row"><span class="bold">EXOTIC</span> <span class="thin">DANCERS</span> | <span class="bold">POLE</span> <span class="thin">DANCERS</span></p>

  <div class="contact">
    <p>To register and more info contact us <strong>glamworks-example.info</strong></p>
    <p><strong>Velvet lantern</strong> 20568 N 14th Ave Franklin,WI 414-555-0193</p>
    <p>Vlx.club/ rickdellano-example.com/cosmicwombat-example.com/ <span class="social-square"></span>/milwaukeevlx</p>
  </div>

  <div class="sponsor-mark">
    <span class="square"></span>
    <span class="name">Cosmic Wombat</span>
  </div>
</main>
</body>
</html>
```